Realty Group Needs Classy, Contemporary Letterhead Design

We need a letterhead design for a new realty company located in NY, USA. We buy investment properties to rehabilitate and or keep in our rental portfolio.

```html
<!DOCTYPE html>
<html lang="en">
<head>
<meta charset="utf-8">
<title>Meridian Realty Group — Letterhead</title>
<link href="https://fonts.googleapis.com/css2?family=Montserrat:wght@500;800&family=Nunito:wght@600&display=swap" rel="stylesheet">
<style>
  :root {
    --purple: #4b2590;
    --grey: #7d7d7d;
    --grey-band: #8a8a8a;
    --ink: #2e2e2e;
    --paper: #ffffff;
    --backdrop: #f1f1f1;
    --emblem: #ececec;
  }
  * { margin: 0; padding: 0; box-sizing: border-box; }
  html, body { width: 1200px; height: 1200px; overflow: hidden; }
  body {
    background: var(--backdrop);
    display: flex;
    align-items: center;
    justify-content: center;
    font-family: "Nunito", sans-serif;
  }
  .letterhead {
    position: relative;
    width: 850px;
    height: 1100px;
    background: var(--paper);
    box-shadow: 0 6px 24px rgba(0,0,0,0.12);
  }
  .header {
    position: absolute;
    top: 78px;
    left: 70px;
    right: 60px;
    display: flex;
    align-items: center;
  }
  .brand { width: 440px; }
  .brand-name {
    font-family: "Montserrat", sans-serif;
    font-weight: 800;
    font-size: 64px;
    letter-spacing: -1px;
    color: var(--purple);
    line-height: 1;
  }
  .brand-tagline {
    display: flex;
    align-items: center;
    gap: 14px;
    margin-top: 6px;
    font-family: "Montserrat", sans-serif;
    font-weight: 500;
    font-size: 20px;
    letter-spacing: 1px;
    color: var(--grey);
  }
  .brand-tagline::before,
  .brand-tagline::after {
    content: "";
    flex: 1;
    height: 2px;
    background: var(--grey);
  }
  .contact {
    margin-left: 28px;
    padding-left: 24px;
    border-left: 2px solid var(--ink);
    font-size: 14.5px;
    line-height: 1.6;
    color: var(--ink);
  }
  .contact-line { display: flex; align-items: center; gap: 6px; }
  .contact-line svg { width: 12px; height: 12px; fill: var(--purple); flex: none; }
  .emblem {
    position: absolute;
    left: 190px;
    top: 330px;
    width: 480px;
    height: 560px;
    border-radius: 50%;
    background: radial-gradient(ellipse at center, var(--emblem) 0%, rgba(236,236,236,0.5) 60%, rgba(255,255,255,0) 75%);
  }
  .footer-band {
    position: absolute;
    left: 0; right: 0; bottom: 0;
    height: 30px;
    display: flex;
    gap: 6px;
  }
  .footer-band .band-grey { flex: 62; background: var(--grey-band); }
  .footer-band .band-purple { flex: 38; background: var(--purple); }
</style>
</head>
<body>
  <main class="letterhead">
    <header class="header">
      <div class="brand">
        <div class="brand-name">MERIDIAN</div>
        <div class="brand-tagline">Realty Group, LLC</div>
      </div>
      <address class="contact" style="font-style:normal">
        <div>2150 Harbor Crest Avenue,</div>
        <div>Suite 410 Lakeview.</div>
        <div class="contact-line">
          <svg viewBox="0 0 16 16"><path d="M3 2h3l1.5 3.5-2 1.3a8 8 0 0 0 3.7 3.7l1.3-2L14 10v3a1 1 0 0 1-1 1A11 11 0 0 1 2 3a1 1 0 0 1 1-1z"/></svg>
          555.204.7788
        </div>
        <div class="contact-line">
          <svg viewBox="0 0 16 16"><path d="M1 3h14v10H1z M1 3l7 5 7-5" stroke="#fff" stroke-width="1"/></svg>
          hello@examplemail.com
        </div>
        <div class="contact-line">
          <svg viewBox="0 0 16 16"><circle cx="8" cy="8" r="7"/><path d="M1 8h14M8 1c3 3 3 11 0 14M8 1c-3 3-3 11 0 14" stroke="#fff" stroke-width="1" fill="none"/></svg>
          www.examplesite.com
        </div>
      </address>
    </header>

    <div class="emblem" role="img" aria-label="Large faint grey brand emblem watermark in the centre of the page"></div>

    <div class="footer-band">
      <div class="band-grey"></div>
      <div class="band-purple"></div>
    </div>
  </main>
</body>
</html>
```